Riverline Estate Holdings Co.

We need a logo and business card design for a Hong Kong based real estate company, KDT Land. We are want the brand to reflect the owners forward thinking, creative, and trend setting projects, while also reflecting a sense of security and strength. We invest in industrial properties which we convert to co-living or co-working spaces. KDT stands for Greater Bay Area which is the region around southern China including HK, Macau, and 9 other Chinese cities...made up of approx. 68 million people. There are massive infrastructure projects including the bridge to Macau and high-speed rail to SZ and the bridge connecting SZ and Zhongshan.

Target Market(s)

Chinese and western retail investors, as well as institutional investors

Industry/Entity Type

Real Estate Development

Contact Information for Business Card

Owen Tallis
CEO
owen@kdtland-hq.com
M + 852 9416 2057
F + 852 3582 0400
Suite 2207, The Meridale, 41 Larchmont Rd., Central, Hong Kong

Logo Text

kdt land (company name) lifestyle property development (underneath)

Colors

Designer to choose colors to be used in the design.

Requirements
Must have
• Details listed above. One side should include the logo and company name...kdt land in modern, hip styling with "lifestyle property development"
Nice to have
• Could be a Black card, with metallic purple "kdt" and white "land"...but open great design ideas
Should not have
• boring and traditional layout

```html
<!DOCTYPE html>
<html lang="en">
<head>
<meta charset="utf-8">
<title>Owen Tallis – KDT Land Business Card</title>
<link href="https://fonts.googleapis.com/css2?family=Jost:wght@400&display=swap" rel="stylesheet">
<style>
  :root {
    --slate: #50646b;
    --charcoal: #26292c;
    --ink: #c9d4d8;
    --icon: #2b2f33;
    --sky-top: #1f4f7a;
    --sky-mid: #6f93b3;
    --tower: #2f3f4c;
  }
  * { margin: 0; padding: 0; box-sizing: border-box; }
  html, body { width: 1200px; height: 700px; overflow: hidden; }
  body { background: var(--charcoal); font-family: "Jost", sans-serif; }
  .card { position: relative; width: 1200px; height: 700px; overflow: hidden; background: var(--charcoal); }
  .card__shapes { position: absolute; inset: 0; }
  .identity { position: absolute; left: 50px; top: 64px; color: var(--ink); }
  .identity__name { font-size: 46px; font-weight: 400; letter-spacing: 0.28em; line-height: 1; }
  .identity__title { font-size: 34px; font-weight: 400; letter-spacing: 0.12em; margin-top: 16px; line-height: 1; }
  .contact { position: absolute; left: 48px; top: 0; list-style: none; color: var(--ink); }
  .contact__item { position: absolute; left: 0; display: flex; white-space: nowrap; }
  .contact__icon { width: 28px; height: 28px; fill: var(--icon); }
  .contact__text { position: absolute; left: 102px; font-size: 21px; letter-spacing: 0.06em; line-height: 29px; }
  .contact__item--email { top: 230px; }
  .contact__item--mobile { top: 336px; }
  .contact__item--fax { top: 434px; }
  .contact__item--address { top: 536px; }
</style>
</head>
<body>
<div class="card">
  <svg class="card__shapes" width="1200" height="700" viewBox="0 0 1200 700">
    <defs>
      <linearGradient id="skyline-tone" x1="0" y1="0" x2="0" y2="1">
        <stop offset="0" stop-color="var(--sky-top)"/>
        <stop offset="0.45" stop-color="var(--sky-mid)"/>
        <stop offset="1" stop-color="var(--tower)"/>
      </linearGradient>
    </defs>
    <polygon points="0,0 845,0 620,350 845,700 0,700" fill="var(--slate)"/>
    <polygon role="img" aria-label="City skyline photograph of modern towers under a blue cloudy sky" points="742,140 1200,140 1200,560 742,560 590,350" fill="url(#skyline-tone)"/>
  </svg>

  <header class="identity">
    <h1 class="identity__name">OWEN TALLIS</h1>
    <p class="identity__title">CEO</p>
  </header>

  <ul class="contact">
    <li class="contact__item contact__item--email">
      <svg class="contact__icon" viewBox="0 0 28 28"><path d="M2 6h24v16H2z M3 7l11 8 11-8" fill="var(--icon)" stroke="var(--slate)" stroke-width="1.4"/></svg>
      <span class="contact__text">OWEN@KDTLAND-HQ.COM</span>
    </li>
    <li class="contact__item contact__item--mobile">
      <svg class="contact__icon" viewBox="0 0 28 28"><path d="M6 3l5 0 2 6-3 2c1.5 3 4 5.5 7 7l2-3 6 2v5c0 1-1 2-2 2C13 24 4 15 4 5c0-1 1-2 2-2z"/></svg>
      <span class="contact__text">852 9416 2057</span>
    </li>
    <li class="contact__item contact__item--fax">
      <svg class="contact__icon" viewBox="0 0 28 28"><path d="M7 2h10l4 4v8H7z M2 16h24v9H2z M4 13h3v3H4z"/></svg>
      <span class="contact__text">852 3582 0400</span>
    </li>
    <li class="contact__item contact__item--address">
      <svg class="contact__icon" viewBox="0 0 28 28"><path d="M14 2c-4.5 0-8 3.5-8 8 0 6 8 16 8 16s8-10 8-16c0-4.5-3.5-8-8-8zm0 11a3 3 0 1 1 0-6 3 3 0 0 1 0 6z"/></svg>
      <span class="contact__text">SUITE 2207, THE MERIDALE,<br>41 LARCHMONT RD.,<br>CENTRAL, HONG KONG</span>
    </li>
  </ul>
</div>
</body>
</html>
```